Startup photography business has a new logo, now we need business cards

Design a business card for the two partners of our business.
Our business Brisk Pelican has a new logo and we need to design a business card to showcase it and us.
Our colours of blue and orange are punchy and vivid, but how can we make the most of it on our card?

It should have our name Brisk Pelican
name of partner
phone number
email
website

Industry/Entity Type

Professional Photography

Contact Information for Business Card

Tom Ashworth
+61 400 55 61 72
tom@briskpelican.com.au
briskpelican.com.au

second card
Neil Porter
+61 400 918 263
neil@briskpelican.com.au
briskpelican.com.au

Colors
f37122
f68d4c
33a6d7
0592cd

Requirements
Must have
• one version of our logo, we have included options
• Name
• phone number
• email
• website
Nice to have
• instagram briskpelicanmedia
• twitter briskpelicanmedia
• facebook briskpelicanmedia

```html
<!DOCTYPE html>
<html lang="en">
<head>
<meta charset="utf-8">
<title>Brisk Pelican — Business Card</title>
<link href="https://fonts.googleapis.com/css2?family=Exo+2:wght@800&family=Lato:wght@400&display=swap" rel="stylesheet">
<style>
  :root {
    --orange: #f37122;
    --orange-soft: #f68d4c;
    --blue: #33a6d7;
    --blue-deep: #0592cd;
    --paper: #fdfdfd;
    --backdrop: #a9a7a8;
    --white: #ffffff;
  }
  * { margin: 0; padding: 0; box-sizing: border-box; }
  html, body { width: 1200px; height: 1200px; overflow: hidden; }
  body { background: var(--backdrop); position: relative; font-family: "Lato", sans-serif; }

  .card {
    position: absolute;
    width: 712px;
    height: 420px;
    background: var(--paper);
    overflow: hidden;
  }
  .card--front { left: 238px; top: 118px; }
  .card--back  { left: 230px; top: 643px; }

  .brand {
    position: absolute;
    display: flex;
    align-items: center;
    gap: 14px;
  }
  .brand__dot {
    width: 44px; height: 44px;
    border-radius: 50%;
    background: var(--orange);
    flex: none;
  }
  .brand__name {
    font-family: "Exo 2", sans-serif;
    font-weight: 800;
    color: var(--blue-deep);
    font-size: 46px;
    letter-spacing: 0.5px;
    white-space: nowrap;
  }
  .card--front .brand { left: 50%; top: 50%; transform: translate(-50%, -50%); }
  .card--back .brand { left: 52px; top: 145px; }
  .card--back .brand__name { font-size: 38px; }
  .card--back .brand__dot { width: 38px; height: 38px; }

  .partner-name {
    position: absolute;
    right: 36px;
    top: 80px;
    font-family: "Exo 2", sans-serif;
    font-weight: 800;
    font-size: 29px;
    color: var(--blue-deep);
    letter-spacing: 0.5px;
    text-transform: uppercase;
  }

  .wave { position: absolute; left: 0; top: 0; width: 712px; height: 420px; }

  .contact {
    position: absolute;
    right: 26px;
    top: 322px;
    list-style: none;
    color: var(--white);
    font-size: 17px;
    line-height: 26px;
    text-align: right;
  }
  .contact__item { display: flex; justify-content: flex-end; align-items: center; gap: 12px; }
  .contact__icon { width: 15px; height: 15px; fill: var(--white); flex: none; }
</style>
</head>
<body>

  <section class="card card--front">
    <div class="brand">
      <span class="brand__dot"></span>
      <span class="brand__name">Brisk Pelican</span>
    </div>
  </section>

  <section class="card card--back">
    <svg class="wave" viewBox="0 0 712 420" aria-hidden="true">
      <path class="wave__blue" d="M0 420 L0 378 C170 410 350 404 480 342 C570 298 640 266 712 254 L712 420 Z" fill="var(--blue-deep)"/>
      <path class="wave__band" d="M0 330 C170 372 340 372 470 312 C570 266 640 240 712 230 L712 242 C640 250 570 276 475 324 C345 386 170 386 0 354 Z" fill="var(--orange)"/>
      <path class="wave__swoosh" d="M70 377 C200 392 330 390 420 362 C330 386 200 389 70 377 Z" fill="var(--orange)"/>
    </svg>

    <div class="brand">
      <span class="brand__dot"></span>
      <span class="brand__name">Brisk Pelican</span>
    </div>

    <h1 class="partner-name">Tom Ashworth</h1>

    <ul class="contact">
      <li class="contact__item">+61 400 55 61 72
        <svg class="contact__icon" viewBox="0 0 16 16"><path d="M2 6 C2 3 14 3 14 6 L11 7 L10 5.5 L6 5.5 L5 7 Z M4 8 L12 8 L14 13 L2 13 Z"/></svg>
      </li>
      <li class="contact__item">briskpelican.com.au
        <svg class="contact__icon" viewBox="0 0 16 16"><circle cx="8" cy="8" r="6.5" fill="none" stroke="#fff" stroke-width="1.4"/><ellipse cx="8" cy="8" rx="2.8" ry="6.5" fill="none" stroke="#fff" stroke-width="1.2"/><path d="M1.5 8 H14.5" stroke="#fff" stroke-width="1.2"/></svg>
      </li>
      <li class="contact__item">tom@briskpelican.com.au
        <svg class="contact__icon" viewBox="0 0 16 16"><path d="M1 3 H15 V13 H1 Z M2 4 L8 9 L14 4" fill="#fff" stroke="var(--blue-deep)" stroke-width="1.2"/></svg>
      </li>
    </ul>
  </section>

</body>
</html>
```